Tozvar new design for business cards we want to change our existing design. Logo must remain the same

Hello we are the company TozVar and offer various services regarding transportation and disposal. In addition to our main acquisition of van rental, we also offer disposal and express transportation, so we need new business card designs for our business. Our elders have their time and do not like it anymore. We want to change our existing design. Logo must remain the same as well as the color blue, whether dark or light Does not play a big role in the best medium blue. Logo must be present on the front side. As well as telephone, email, web and location. Big enough but not too big. Back can be redesigned Logo as well as name TozVar must be present. Important is the text: Van rental Disposal and clearing express transportation. Without bail in red should be noted somewhere. it should be modern but not too playful. rather serious but no beating company Thank you very much

Target Market(s)

Private customers as well as companies we want to change our existing design. Logo must remain the same as well as the color blue, whether dark or light Does not play a big role in the best medium blue. Logo must be present on the front side. As well as telephone, email, web and location. Big enough but not too big. Back can be redesigned Logo as well as name TozVar must be present. Important is the text: Van rental Disposal and clearing express transportation. Without bail in red should be noted somewhere. it should be modern but not too playful. rather serious but no beating company Thank you very much

Industry/Entity Type

Car Rental

Contact Information for Business Card

we want to change our existing design. Logo must remain the same as well as the color blue, whether dark or light Does not play a big role in the best medium blue.
Logo must be present on the front side.
As well as telephone, email, web and location. Big enough but not too big.
Back can be redesigned Logo as well as name TozVar must be present.
Important is the text:
Van rental
Disposal and clearing
Express transportation.
Without bail in red should be noted somewhere.
it should be modern but not too playful. rather serious but no beating company
Thank you very much

Font styles to use
Sans Serif

Colors
33a6d7
ec1f27
0692cd
3277b5

Requirements
Must have
• logo and name TozVar as described in the above text must have it. we want to change our existing design. Logo must remain the same as well as the color blue, whether dark or light Does not play a big role in the best medium blue. Logo must be present on the front side. As well as telephone, email, web and location. Big enough but not too big. Back can be redesigned Logo as well as name TozVar must be present. Important is the text: Van rental Disposal and clearing express transportation. Without bail in red should be noted somewhere. it should be modern but not too playful. rather serious but no beating company Thank you very much
Nice to have
• see description we want to change our existing design. Logo must remain the same as well as the color blue, whether dark or light Does not play a big role in the best medium blue. Logo must be present on the front side. As well as telephone, email, web and location. Big enough but not too big. Back can be redesigned Logo as well as name TozVar must be present. Important is the text: Van rental Disposal and clearing express transportation. Without bail in red should be noted somewhere. it should be modern but not too playful. rather serious but no beating company Thank you very much
Should not have
• Blue White and little red we want to change our existing design. Logo must remain the same as well as the color blue, whether dark or light Does not play a big role in the best medium blue. Logo must be present on the front side. As well as telephone, email, web and location. Big enough but not too big. Back can be redesigned Logo as well as name TozVar must be present. Important is the text: Van rental Disposal and clearing express transportation. Without bail in red should be noted somewhere. it should be modern but not too playful. rather serious but no beating company Thank you very much

```html
<!DOCTYPE html>
<html lang="en">
<head>
<meta charset="utf-8">
<title>TozVar business cards</title>
<link rel="stylesheet" href="https://fonts.googleapis.com/css2?family=Arimo:wght@400;700&display=swap">
<style>
  :root {
    --bg: #2a2b2d;
    --navy: #1b1f78;
    --slate: #7f9ab4;
    --slate-light: #8aa4bd;
    --slate-dark: #5d7893;
    --paper: #fbfbfc;
    --paper-shade: #e9ecef;
    --ink: #1d1d1f;
    --white: #ffffff;
    --alert: #ec1f27;
  }
  * { box-sizing: border-box; margin: 0; padding: 0; }
  html, body { width: 1200px; height: 997px; overflow: hidden; }
  body {
    background: var(--bg);
    font-family: "Arimo", Arial, sans-serif;
    position: relative;
  }
  .card {
    position: absolute;
    width: 540px;
    height: 310px;
    border-radius: 4px;
    overflow: hidden;
    box-shadow: 0 10px 30px rgba(0,0,0,.45);
  }

  /* brand lockup */
  .brand { display: flex; align-items: center; gap: 12px; }
  .brand-square { width: 44px; height: 44px; flex: none; }
  .brand-name { font-weight: 700; font-size: 38px; letter-spacing: 1px; line-height: 1; }
  .brand-suffix { font-weight: 700; font-size: 9px; letter-spacing: .5px; align-self: flex-start; margin-left: -8px; }

  /* back side */
  .card-back {
    left: 40px; top: 344px;
    background: linear-gradient(180deg, var(--slate-light) 0%, var(--slate) 100%);
  }
  .card-back .brand { position: absolute; left: 120px; top: 96px; }
  .card-back .brand-square { background: var(--white); }
  .card-back .brand-name,
  .card-back .brand-suffix { color: var(--white); }
  .services {
    position: absolute; left: 120px; top: 170px;
    list-style: none; color: var(--white);
    font-size: 14px; line-height: 1.55;
  }
  .deposit-note {
    position: absolute; left: 120px; top: 252px;
    color: var(--alert); font-weight: 700; font-size: 13px;
    background: var(--white); padding: 3px 8px; border-radius: 2px;
  }

  /* front side */
  .card-front {
    left: 620px; top: 344px;
    background: linear-gradient(160deg, var(--paper) 0%, var(--paper-shade) 100%);
  }
  .card-front .brand { position: absolute; left: 150px; top: 56px; }
  .card-front .brand-square { background: var(--navy); }
  .card-front .brand-name,
  .card-front .brand-suffix { color: var(--navy); }
  .rule { position: absolute; height: 1px; background: var(--ink); }
  .rule-logo { left: 210px; right: 22px; top: 116px; }
  .holder { position: absolute; left: 26px; top: 166px; }
  .holder-name { color: var(--navy); font-size: 19px; }
  .holder-role { color: var(--slate-dark); font-size: 12px; margin-top: 1px; }
  .rule-name { left: 150px; right: 22px; top: 181px; }
  .address {
    position: absolute; right: 24px; top: 196px;
    text-align: right; font-size: 12.5px; color: var(--ink); line-height: 1.35;
  }
  .contact { position: absolute; left: 26px; top: 218px; list-style: none; }
  .contact li { display: flex; align-items: center; gap: 10px; font-size: 14px; color: var(--ink); height: 24px; }
  .contact svg { width: 14px; height: 14px; }
  .bands { position: absolute; left: 0; bottom: 0; width: 540px; height: 310px; }
  .web {
    position: absolute; right: 24px; top: 264px;
    font-weight: 700; font-size: 13px; letter-spacing: 2px; color: var(--navy);
  }
</style>
</head>
<body>
  <section class="card card-back" aria-label="Card back">
    <div class="brand">
      <span class="brand-square"></span>
      <span class="brand-name">TOZVAR</span>
      <span class="brand-suffix">GMBH</span>
    </div>
    <ul class="services">
      <li>Van rental</li>
      <li>Disposal and clearing</li>
      <li>Express transportation</li>
    </ul>
    <p class="deposit-note">Without bail</p>
  </section>

  <section class="card card-front" aria-label="Card front">
    <svg class="bands" viewBox="0 0 540 310" aria-hidden="true">
      <path d="M0,292 L300,292 C318,292 318,258 342,258 L540,258 L540,310 L0,310 Z" fill="var(--slate)"/>
      <path d="M0,283 L292,283 C306,283 308,268 314,262" fill="none" stroke="var(--navy)" stroke-width="6"/>
    </svg>

    <div class="brand">
      <span class="brand-square"></span>
      <span class="brand-name">TOZVAR</span>
      <span class="brand-suffix">GMBH</span>
    </div>
    <div class="rule rule-logo"></div>

    <div class="holder">
      <p class="holder-name">Marcus Hale</p>
      <p class="holder-role">Director</p>
    </div>
    <div class="rule rule-name"></div>

    <p class="address">P.O. Box KL318, Kelmore<br>KL 04, Bermuda</p>

    <ul class="contact">
      <li>
        <svg viewBox="0 0 14 14" aria-hidden="true"><circle cx="7" cy="7" r="7" fill="var(--slate)"/><path d="M4.5 4 L6 4 L6.5 5.6 L5.6 6.3 Q6.3 7.7 7.7 8.4 L8.4 7.5 L10 8 L10 9.5 Q6 10 4.5 4 Z" fill="var(--white)"/></svg>
        <span>1 441 555 0147</span>
      </li>
      <li>
        <svg viewBox="0 0 14 14" aria-hidden="true"><circle cx="7" cy="7" r="7" fill="var(--slate)"/><rect x="3.5" y="4.5" width="7" height="5" fill="none" stroke="var(--white)" stroke-width="1"/><path d="M3.5 4.5 L7 7.3 L10.5 4.5" fill="none" stroke="var(--white)" stroke-width="1"/></svg>
        <span>mhale@harbourline.bm</span>
      </li>
    </ul>

    <p class="web">WWW.TOZVAR.COM</p>
  </section>
</body>
</html>
```